New Website

New website is to be the same as Valiant Oak.

Website needs to be fully functional, with only text and logo to be added by client at a later date.

Logo has been added for reference.

Coding

Coded - Design and coding required

```html
<!DOCTYPE html>
<html lang="en">
<head>
<meta charset="utf-8">
<title>Brightlane – Internet Publishing and Online Marketing</title>
<link rel="stylesheet" href="https://fonts.googleapis.com/css2?family=Mulish:wght@400;600;700&display=swap">
<style>
  :root {
    --dark: #333433;
    --hero: #353635;
    --white: #ffffff;
    --nav-text: #8a8a8a;
    --muted: #8c8c8c;
    --heading: #444444;
    --card-bg: #efefef;
    --card-border: #cfcfcf;
    --green: #0db02b;
    --icon-dark: #2e2f2e;
  }
  * { box-sizing: border-box; margin: 0; padding: 0; }
  html, body { width: 1200px; height: 1200px; overflow: hidden; }
  body { position: relative; background: var(--white); font-family: "Mulish", sans-serif; color: var(--muted); }

  .topbar { position: absolute; left: 0; top: 0; width: 1200px; height: 50px; background: var(--dark); }
  .brand { position: absolute; left: 105px; top: 11px; font-size: 24px; font-weight: 700; color: var(--white); letter-spacing: 0.3px; }
  .search { position: absolute; left: 909px; top: 10px; display: flex; height: 27px; }
  .search-field { width: 136px; background: var(--white); border-radius: 4px 0 0 4px; font-size: 13px; color: #999; padding: 5px 14px; }
  .search-btn { width: 50px; background: var(--green); color: var(--white); font-size: 13px; border-radius: 0 4px 4px 0; text-align: center; padding-top: 5px; }

  .mainnav { position: absolute; left: 0; top: 50px; width: 1200px; height: 55px; display: flex; justify-content: flex-end; align-items: center; padding-right: 46px; gap: 40px; }
  .mainnav a { color: var(--nav-text); text-decoration: none; font-size: 16px; }

  .hero { position: absolute; left: 0; top: 105px; width: 1200px; height: 323px; background: var(--hero); }
  .hero-art { position: absolute; left: 104px; top: 95px; width: 440px; height: 205px; border-radius: 100px; background: radial-gradient(circle at 42% 50%, #4fae2f 0%, #2f7d24 28%, #3f4a3c 55%, var(--hero) 75%); }
  .hero-title { position: absolute; left: 600px; top: 58px; font-size: 26px; line-height: 33px; font-weight: 400; color: var(--white); }
  .hero-points { position: absolute; left: 600px; top: 160px; list-style: none; color: var(--white); font-size: 13.5px; line-height: 27px; }

  .service { position: absolute; top: 448px; width: 147px; height: 288px; background: var(--card-bg); border: 3px solid var(--card-border); border-bottom: none; border-radius: 6px 6px 0 0; text-align: center; }
  .service.is-active { background: var(--white); height: 328px; border-bottom: none; z-index: 2; }
  .service-icon { display: block; margin: 4px auto 0; }
  .service.is-active .service-icon { margin-top: 24px; }
  .service-name { font-size: 21px; font-weight: 400; color: var(--muted); margin: 12px 0 12px; }
  .service-text { font-size: 13.5px; line-height: 17.3px; color: var(--muted); padding: 0 2px; }

  .talent { position: absolute; left: 105px; top: 734px; width: 996px; height: 380px; border: 3px solid var(--card-border); border-radius: 8px; }
  .talent-title { position: absolute; left: 0; top: 44px; width: 100%; text-align: center; font-size: 20px; font-weight: 400; color: var(--muted); }
  .job-btn { position: absolute; left: 357px; top: 86px; width: 221px; height: 48px; background: var(--green); color: var(--white); font-size: 23px; text-align: center; line-height: 48px; border-radius: 3px; text-decoration: none; }

  .feature { position: absolute; top: 174px; width: 250px; }
  .feature-icon { position: absolute; left: 0; top: 0; }
  .feature-title { position: absolute; top: 6px; font-size: 16px; font-weight: 600; color: var(--heading); white-space: nowrap; }
  .feature-text { position: absolute; top: 40px; width: 170px; font-size: 13.5px; line-height: 17.3px; color: var(--muted); }
  .feature-link { position: absolute; top: 154px; font-size: 13.5px; color: var(--muted); }

  .footer { position: absolute; left: 0; top: 1145px; width: 1200px; height: 55px; background: var(--dark); color: var(--white); }
  .copyright { position: absolute; left: 110px; top: 14px; font-size: 11.5px; }
  .coverage { position: absolute; right: 110px; top: 15px; font-size: 9px; letter-spacing: -0.2px; }
</style>
</head>
<body>
  <header class="topbar">
    <div class="brand">Brightlane</div>
    <div class="search"><div class="search-field">Enter your text</div><div class="search-btn">Search</div></div>
  </header>

  <nav class="mainnav">
    <a href="#">Home</a><a href="#">Abou Us</a><a href="#">Carrier</a><a href="#">Contact Us</a><a href="#">Blogs</a>
  </nav>

  <section class="hero">
    <div class="hero-art" role="img" aria-label="Illustration of a glossy green globe with an exclamation mark, a question bubble and small figures"></div>
    <h1 class="hero-title">Internet Publishing and Online<br>Marketing at its Best!</h1>
    <ul class="hero-points">
      <li>A wide range of verticals like Health, Education, Finance, Travel, Fitness!</li>
      <li>Proprietary Traffic Management Platform</li>
      <li>Specialists in Pay Per Click, Cost Per Action, Lead Generation, and SEO!</li>
    </ul>
  </section>

  <article class="service is-active" style="left:106px">
    <svg class="service-icon" width="66" height="66" viewBox="0 0 66 66"><circle cx="33" cy="33" r="33" fill="var(--icon-dark)"/><circle cx="33" cy="33" r="17" fill="none" stroke="#fff" stroke-width="2.5"/><path d="M22 26 q6-4 10 0 q2 5-3 7 q2 6-3 9 q-3-6-4-10z M36 20 q6 0 9 6 q-4 2-7 0z M38 34 q6-2 8 4 q-3 6-7 6 q0-5-1-10z" fill="#fff"/></svg>
    <h2 class="service-name">Publishing</h2>
    <p class="service-text">Our online publishing team manages a portfolio of over a dozen properties that receive over 100,000 combined unique users daily and growing!</p>
  </article>

  <article class="service" style="left:274px">
    <svg class="service-icon" width="66" height="66" viewBox="0 0 66 66"><circle cx="33" cy="33" r="33" fill="var(--icon-dark)"/><circle cx="33" cy="26" r="3" fill="#fff"/><path d="M26 19 a10 10 0 0 0 0 14 M40 19 a10 10 0 0 1 0 14 M21 15 a16 16 0 0 0 0 22 M45 15 a16 16 0 0 1 0 22" fill="none" stroke="#fff" stroke-width="2.5"/><path d="M33 29 L26 50 M33 29 L40 50 M29 42 h8" stroke="#fff" stroke-width="2.5" fill="none"/></svg>
    <h2 class="service-name">XML</h2>
    <p class="service-text">Our online publishing team manages a portfolio of over a dozen properties that receive over 100,000 combined unique users daily and growing!</p>
  </article>

  <article class="service" style="left:442px">
    <svg class="service-icon" width="66" height="66" viewBox="0 0 66 66"><circle cx="33" cy="33" r="33" fill="var(--icon-dark)"/><path d="M14 27 l10-9 v5 h16 v8 h-16 v5z M52 39 l-10-9 v5 h-16 v8 h16 v5z" fill="#fff"/></svg>
    <h2 class="service-name">CPA</h2>
    <p class="service-text">Our online publishing team manages a portfolio of over a dozen properties that receive over 100,000 combined unique users daily and growing!</p>
  </article>

  <article class="service" style="left:610px">
    <svg class="service-icon" width="66" height="66" viewBox="0 0 66 66"><circle cx="33" cy="33" r="33" fill="var(--icon-dark)"/><rect x="18" y="20" width="30" height="21" rx="2" fill="none" stroke="#fff" stroke-width="2.5"/><path d="M14 44 h38 v3 h-38z" fill="#fff"/><path d="M32 26 l0 10 l3-3 l3 4 l2-1 l-3-4 l4-1z" fill="#fff"/></svg>
    <h2 class="service-name">PPC</h2>
    <p class="service-text">Our online publishing team manages a portfolio of over a dozen properties that receive over 100,000 combined unique users daily and growing!</p>
  </article>

  <article class="service" style="left:778px">
    <svg class="service-icon" width="66" height="66" viewBox="0 0 66 66"><circle cx="33" cy="33" r="33" fill="var(--icon-dark)"/><circle cx="33" cy="33" r="18" fill="none" stroke="#fff" stroke-width="2.5"/><ellipse cx="33" cy="33" rx="18" ry="7" fill="none" stroke="#fff" stroke-width="2" transform="rotate(35 33 33)"/><ellipse cx="33" cy="33" rx="18" ry="7" fill="none" stroke="#fff" stroke-width="2" transform="rotate(-35 33 33)"/></svg>
    <h2 class="service-name">SEO</h2>
    <p class="service-text">Our online publishing team manages a portfolio of over a dozen properties that receive over 100,000 combined unique users daily and growing!</p>
  </article>

  <article class="service" style="left:946px">
    <svg class="service-icon" width="66" height="66" viewBox="0 0 66 66"><circle cx="33" cy="33" r="33" fill="var(--icon-dark)"/><path d="M14 27 l10-9 v5 h16 v8 h-16 v5z M52 39 l-10-9 v5 h-16 v8 h16 v5z" fill="#fff"/></svg>
    <h2 class="service-name">Publish Tool</h2>
    <p class="service-text">Our online publishing team manages a portfolio of over a dozen properties that receive over 100,000 combined unique users daily and growing!</p>
  </article>

  <section class="talent">
    <h2 class="talent-title">Corvane Is Always On The Lookout For New Talent!</h2>
    <a class="job-btn" href="#">Looking For A Job?</a>

    <div class="feature" style="left:22px">
      <svg class="feature-icon" width="66" height="50" viewBox="0 0 66 50"><circle cx="16" cy="12" r="9" fill="var(--green)"/><circle cx="50" cy="12" r="9" fill="var(--green)"/><path d="M2 38 q2-14 14-14 q12 0 14 14z M36 38 q2-14 14-14 q12 0 14 14z" fill="var(--green)"/><circle cx="33" cy="14" r="11" fill="var(--green)" stroke="#fff" stroke-width="2"/><path d="M15 48 q2-20 18-20 q16 0 18 20z" fill="var(--green)" stroke="#fff" stroke-width="2"/></svg>
      <h3 class="feature-title" style="left:69px">Who We Are</h3>
      <p class="feature-text" style="left:74px">We're comprised of a team of highly skilled developers, enthusiastic designers, smart content writers and innovative online marketers.</p>
      <a class="feature-link" href="#" style="left:74px">continue reading</a>
    </div>

    <div class="feature" style="left:356px">
      <svg class="feature-icon" width="50" height="50" viewBox="0 0 50 50"><path d="M30 8 h-24 v38 h36 v-22" fill="none" stroke="var(--green)" stroke-width="5"/><path d="M40 2 l8 8 l-22 22 l-11 3 l3-11z" fill="var(--green)"/></svg>
      <h3 class="feature-title" style="left:54px">Contact Us</h3>
      <p class="feature-text" style="left:59px">We leverage targeted traffic using Search Engine Marketing (SEM), Search Engine Optimization (SEO), Social Media and more.</p>
      <a class="feature-link" href="#" style="left:59px">continue reading</a>
    </div>

    <div class="feature" style="left:670px">
      <svg class="feature-icon" width="44" height="46" viewBox="0 0 44 46"><rect x="18" y="0" width="6" height="46" fill="var(--green)"/><path d="M6 6 h34 l4 5 l-4 5 h-34z" fill="var(--green)"/><path d="M38 20 h-34 l-4 5 l4 5 h34z" fill="var(--green)"/></svg>
      <h3 class="feature-title" style="left:48px">Careers</h3>
      <p class="feature-text" style="left:53px">A highly competent team, great benefits and a stellar location in the centre of Elmford, make Corvane is a great place to work.</p>
      <a class="feature-link" href="#" style="left:53px">continue reading</a>
    </div>
  </section>

  <footer class="footer">
    <p class="copyright">Copyright © Brightlane.net All rights reserved</p>
    <p class="coverage">Brightlane Staffer is serving USA, Europe, Australia and Central America.</p>
  </footer>
</body>
</html>
```